Med Spa business card design with logo

Need a logo design and business card for our new company Verbena Aesthetics Med Spa. We are a medical office that deals with high end clients. We offer them skin care products which include DERMIQ, lip augmentation, and various laser for the skin. I king of like the logo attached, maybe something along those lines but also open to any logo concept.
Updates

Target Market(s)

Out target audience are male and females in the age range of 21-80 years of age

Industry/Entity Type

Medical

Contact Information for Business Card

woukd like front of card to have logo and business name VERBENA AESTHETICS MEDSPA. Back of card employee name and phone number along with instagram logo and user name

Font styles to use
Serif
Sans Serif

Requirements
Must have
• prefer monochromatic look white, black, gold
Should not have
• not too colorful

```html
<!DOCTYPE html>
<html lang="en">
<head>
<meta charset="utf-8">
<title>Verbena Aesthetics Med Spa – Business Card</title>
<link rel="stylesheet" href="https://fonts.googleapis.com/css2?family=Open+Sans:wght@300;400;600;700&display=swap">
<style>
  :root {
    --backdrop: #ecebe9;
    --card-white: #f7f7f5;
    --card-dark: #3a3a3a;
    --band: #cfcfcf;
    --ink: #3c3c3c;
    --ink-soft: #5a5a5a;
    --on-dark: #ececec;
    --mark-ring: #9a9a9a;
  }
  * { margin: 0; padding: 0; box-sizing: border-box; }
  html, body {
    width: 1200px; height: 844px; overflow: hidden;
    background: var(--backdrop);
    font-family: "Open Sans", Arial, sans-serif;
    color: var(--ink);
  }
  .stage { position: relative; width: 1200px; height: 844px; }

  .card {
    position: absolute; top: 280px;
    width: 500px; height: 286px;
    box-shadow: 0 6px 18px rgba(0,0,0,0.18);
  }

  /* Back: contact side */
  .card-contact { left: 70px; background: var(--card-white); }
  .brand {
    position: absolute; right: 34px; top: 34px;
    display: flex; flex-direction: column; align-items: center;
  }
  .brand-circle {
    width: 62px; height: 62px; border-radius: 50%;
    border: 2px solid var(--mark-ring);
    margin-bottom: 12px;
  }
  .brand-name {
    font-weight: 300; font-size: 23px; letter-spacing: 1.5px;
    color: var(--ink); text-align: center; line-height: 1.2;
  }
  .contact { position: absolute; left: 34px; bottom: 30px; }
  .person-name { font-weight: 700; font-size: 15px; letter-spacing: 0.5px; color: var(--ink-soft); }
  .person-role { font-size: 12px; color: var(--ink-soft); margin-bottom: 16px; }
  .handle-row, .detail-row {
    display: flex; align-items: center; gap: 8px;
    font-size: 13px; color: var(--ink-soft);
  }
  .handle-row { margin-bottom: 12px; }
  .detail-row { gap: 14px; }
  .icon-square {
    width: 16px; height: 16px; border-radius: 3px;
    background: var(--ink-soft);
  }

  /* Front: logo side */
  .card-logo { left: 630px; background: var(--card-dark); }
  .stripe-band {
    position: absolute; left: 0; right: 0; top: 78px; height: 78px;
    background: var(--band);
  }
  .emblem {
    position: absolute; left: 50%; top: 38px; transform: translateX(-50%);
    width: 158px; height: 158px; border-radius: 50%;
    background: var(--card-dark);
    display: flex; align-items: center; justify-content: center;
    text-align: center;
  }
  .emblem-name {
    font-weight: 300; font-size: 13px; letter-spacing: 1.5px;
    color: var(--on-dark); line-height: 1.35;
  }
  .card-logo .handle-row {
    position: absolute; left: 0; right: 0; bottom: 40px;
    justify-content: center; color: var(--on-dark); margin: 0;
  }
  .card-logo .icon-square { background: var(--on-dark); }
</style>
</head>
<body>
<main class="stage">
  <section class="card card-contact">
    <div class="brand">
      <div class="brand-circle"></div>
      <div class="brand-name">VERBENA AESTHETICS<br>MEDSPA</div>
    </div>
    <div class="contact">
      <p class="person-name">MARCUS HALE</p>
      <p class="person-role">Managing Director</p>
      <p class="handle-row"><span class="icon-square"></span>/verbenaaestheticsmedspa</p>
      <p class="detail-row"><span>P: 555-318-2047</span><span>E: hello@verbenamedspa.com</span></p>
    </div>
  </section>

  <section class="card card-logo">
    <div class="stripe-band"></div>
    <div class="emblem">
      <p class="emblem-name">VERBENA<br>AESTHETICS<br>MEDSPA</p>
    </div>
    <p class="handle-row"><span class="icon-square"></span>/verbenaaestheticsmedspa</p>
  </section>
</main>
</body>
</html>
```